R & K Fabworks Brochure

We need a 2 page (front and back) full color brochure for our Mechanical Contracting company. The website is http://www.rkfabworks.example although we're looking for something fresh. If anything the future web design might follow the design of this brochure more than we'd like to have the brochure follow the design of the website. However, to start please use content found on the website and we will refine. We want basically a cover, 2 inner pages and a back. Attached is a an example brochure from another company as well as an outdated brochure we used previously.

Target Market(s)

1. Industrial, Commercial and Institutional Builders and Owners

2. Industrial, Commercial and Institutional HVAC Service customers

Industry/Entity Type

It Company

Font styles to use
Serif
Sans Serif

Requirements
Must have
• Strong imagery
Should not have
• Plumbing Service
Pictures of people besides Owner Marlon Quigsby and President Dustin Okafor

```html
<!DOCTYPE html>
<html lang="en">
<head>
<meta charset="utf-8">
<title>R &amp; K Fabworks Brochure</title>
<link rel="stylesheet" href="https://fonts.googleapis.com/css2?family=Oswald:wght@400;500&family=Open+Sans:ital,wght@0,400;0,700;1,700&display=swap">
<style>
  :root {
    --charcoal: #2b2b2c;
    --charcoal-deep: #1c1c1d;
    --brand-blue: #2a68b4;
    --brand-blue-deep: #1b4f93;
    --accent-red: #c8242b;
    --pipe-red: #d8333a;
    --pipe-cream: #e9dcc4;
    --white: #ffffff;
    --text-light: #e6e6e6;
  }
  * { margin: 0; padding: 0; box-sizing: border-box; }
  html, body { width: 1200px; height: 869px; overflow: hidden; background: #f2f2f2; }
  .brochure { position: relative; width: 1200px; height: 869px; overflow: hidden; font-family: "Open Sans", Arial, sans-serif; }
  .backdrop { position: absolute; inset: 0; }
  .about-heading {
    position: absolute; left: 30px; top: 40px;
    font-family: "Oswald", "Arial Narrow", sans-serif; font-weight: 400;
    font-size: 22px; color: var(--white); letter-spacing: -0.2px;
  }
  .about-rule { position: absolute; left: 30px; top: 82px; width: 202px; height: 1px; background: var(--text-light); }
  .about-copy {
    position: absolute; left: 30px; top: 104px; width: 350px;
    color: var(--text-light); font-size: 12.4px; line-height: 20px;
    text-align: justify; hyphens: auto;
  }
  .about-copy p + p { margin-top: 20px; }
  .name-mark {
    position: absolute; display: flex; align-items: center; gap: 10px;
    font-family: "Oswald", "Arial Narrow", sans-serif; font-weight: 500;
    color: var(--white); white-space: nowrap;
  }
  .name-mark .square { display: block; background: var(--brand-blue); border: 2px solid var(--white); }
  .name-mark--back { left: 34px; top: 752px; font-size: 28px; }
  .name-mark--back .square { width: 26px; height: 26px; }
  .name-mark--cover { left: 900px; top: 670px; font-size: 38px; }
  .name-mark--cover .square { width: 36px; height: 36px; }
  .contact {
    position: absolute; right: 627px; top: 706px; text-align: right;
    color: var(--white); font-size: 13.5px; font-weight: 700; line-height: 17px;
  }
  .contact-company { font-style: italic; font-size: 16px; letter-spacing: 0.4px; margin-bottom: 15px; }
  .contact-line { display: flex; justify-content: flex-end; align-items: flex-start; gap: 5px; margin-bottom: 13px; }
  .contact-line svg { flex: none; margin-top: 2px; }
  .cover-title {
    position: absolute; right: 48px; top: 470px; text-align: right;
    font-family: "Oswald", "Arial Narrow", sans-serif; font-weight: 400;
    font-size: 38px; line-height: 46px; color: var(--white);
  }
  .cover-web {
    position: absolute; right: 48px; top: 797px;
    font-family: "Oswald", "Arial Narrow", sans-serif; font-weight: 400;
    font-size: 31px; color: var(--white);
  }
</style>
</head>
<body>
<main class="brochure">
  <svg class="backdrop" width="1200" height="869" viewBox="0 0 1200 869" aria-hidden="false">
    <defs>
      <linearGradient id="photoTone" x1="0" y1="0" x2="1" y2="1">
        <stop offset="0" stop-color="#b8232a"/>
        <stop offset="0.45" stop-color="#e3d3b8"/>
        <stop offset="0.7" stop-color="#d8333a"/>
        <stop offset="1" stop-color="#8e1d22"/>
      </linearGradient>
      <radialGradient id="charcoalGlow" cx="0.45" cy="0.45" r="0.7">
        <stop offset="0" stop-color="#3a3a3b"/>
        <stop offset="1" stop-color="#1c1c1d"/>
      </radialGradient>
      <radialGradient id="blueGlow" cx="0.6" cy="0.5" r="0.8">
        <stop offset="0" stop-color="#3273c2"/>
        <stop offset="1" stop-color="#1b4f93"/>
      </radialGradient>
    </defs>
    <rect class="photo-area" x="400" y="0" width="800" height="520" fill="url(#photoTone)" role="img" aria-label="Photograph of red and cream insulated industrial pipework with valves in a mechanical room"/>
    <path class="cover-blue" d="M1200 372 C950 380 720 430 580 540 C460 640 340 770 290 869 L1200 869 Z" fill="url(#blueGlow)"/>
    <path class="back-panel" d="M0 0 L445 0 C560 120 640 300 625 470 C610 620 430 760 290 869 L0 869 Z" fill="url(#charcoalGlow)"/>
    <path class="swoosh-red" d="M150 0 C300 10 420 60 500 150 C440 90 330 30 150 0 Z" fill="var(--accent-red)"/>
    <path class="swoosh-dark" d="M200 0 C330 20 440 80 520 175 C450 105 350 40 200 0 Z" fill="var(--charcoal-deep)"/>
    <path class="swoosh-blue" d="M1200 392 C900 380 620 450 470 600 C380 690 320 760 300 800 C340 740 420 660 500 590 C650 470 920 400 1200 410 Z" fill="var(--brand-blue)"/>
    <path class="swoosh-blue-thin" d="M1200 360 C950 362 720 410 590 500" fill="none" stroke="#3a79c9" stroke-width="4"/>
    <line x1="600" y1="0" x2="600" y2="869" stroke="#000" stroke-opacity="0.12" stroke-width="1"/>
  </svg>

  <h2 class="about-heading">ABOUT US</h2>
  <div class="about-rule"></div>
  <div class="about-copy">
    <p>R &amp; K Fabworks designs, builds, installs and services Heating, Ventilation and Air Conditioning (HVAC) and Plumbing systems for commercial, industrial and residential applications. For over 100 years, R &amp; K Fabworks has built a solid reputation on doing the job right, the first time. R &amp; K Fabworks employs 130 people; 105 in the field and 25 office staff. Of our $30+ million in annual sales, 90% is mechanical, and 10% is plumbing. R &amp; K is a union contractor with ongoing labor agreements with the Steamfitters, Plumbers, and Sheetmetal workers. These Unions give us the manpower and training we need to provide staffing for projects of all sizes.</p>
    <p>100 years of service has taught us that you can’t do work that will stand the test of time unless you use materials that will stand the test of time. We combine an old fashioned devotion to good business practices and superior materials with a youthful approach to conserving energy, cutting costs and improving efficiency. R &amp; K takes pride in completing high-quality projects on time and under budget. Our on-site fabrication and manufacturing facilities are the finest in the industry, helping us keep up with the material demands of any size project while controlling quality and costs.</p>
  </div>

  <div class="name-mark name-mark--back"><span class="square"></span>R &amp; K Fabworks</div>

  <address class="contact">
    <div class="contact-company">R &amp; K FABWORKS, INC.</div>
    <div class="contact-line">
      <svg width="10" height="13" viewBox="0 0 10 13"><path d="M5 0 C2.2 0 0 2.2 0 4.8 C0 8.3 5 13 5 13 C5 13 10 8.3 10 4.8 C10 2.2 7.8 0 5 0 Z M5 6.6 A1.8 1.8 0 1 1 5 3 A1.8 1.8 0 1 1 5 6.6 Z" fill="#fff"/></svg>
      <span>4470 Alder Creek Road Fairview,<br>WI 53999</span>
    </div>
    <div class="contact-line">
      <svg width="13" height="13" viewBox="0 0 13 13"><circle cx="6.5" cy="6.5" r="5.8" fill="none" stroke="#fff" stroke-width="1.2"/><path d="M4.2 3.4 L5.4 3.2 L6 4.8 L5.2 5.5 C5.6 6.5 6.4 7.3 7.4 7.8 L8.1 7 L9.7 7.6 L9.5 8.8 C7 9.2 3.6 5.8 4.2 3.4 Z" fill="#fff"/></svg>
      <span>555-014-3434</span>
      <svg width="15" height="12" viewBox="0 0 15 12" style="margin-left:6px"><path d="M2 5 L3.5 1.2 H11.5 L13 5 H14.5 V9.5 H13 V11.5 H11 V9.5 H4 V11.5 H2 V9.5 H0.5 V5 Z M3.5 5 H11.5 L10.6 2.6 H4.4 Z" fill="#fff"/></svg>
      <span>555-014-9654</span>
    </div>
    <div class="contact-line">
      <svg width="13" height="13" viewBox="0 0 13 13" fill="none" stroke="#fff" stroke-width="1.1"><circle cx="6.5" cy="6.5" r="5.8"/><ellipse cx="6.5" cy="6.5" rx="2.6" ry="5.8"/><line x1="0.7" y1="6.5" x2="12.3" y2="6.5"/></svg>
      <span>www.rkfabworks.example</span>
    </div>
  </address>

  <h1 class="cover-title">COMPLETE MECHANICAL<br>CONTRACTING SERVICE</h1>
  <div class="name-mark name-mark--cover"><span class="square"></span>R &amp; K Fabworks</div>
  <div class="cover-web">www.rkfabworks.example</div>
</main>
</body>
</html>
```